French Bistro Needs a Menu Design for Grand Opening.

We need a menu design incorporating our logo as a design element into the design. The menu needs to be front and back in a 8.5 x 11 inch format. The front of the menu should break up the page into categories for Cocktails, Wines by the Glass, Zero Proof Options, and other beverages.
The back of the menu should break up the page into categories for Appetizers, Charcuterie, Soups and Salads and Entrees.

Here are a few examples of some of the design elements we are interested in. The menu can be either portrait or landscape format.
Thanks,
Calvin

file:///C:/Users/Tomsv/Downloads/Brisol%20Menu.webp

https://img.picvaultexample.net/set/ref-menu-sample-01.jpg

https://img.picvaultexample.net/set/ref-menu-sample-02.jpg

```html
<!DOCTYPE html>
<html lang="en">
<head>
<meta charset="utf-8">
<title>Bistro Marlowe — Drinks &amp; Food Menu</title>
<link href="https://fonts.googleapis.com/css2?family=Cinzel:wght@500&family=Oswald:wght@500;600&family=Roboto+Condensed:wght@500&family=Zilla+Slab:wght@600;700&family=Poppins:wght@400&display=swap" rel="stylesheet">
<style>
  :root{
    --backdrop:#808080;
    --paper:#fbf3e1;
    --gold:#c6a866;
    --gold-soft:rgba(198,168,102,.35);
    --ink:#242424;
    --ink-soft:#3a3a3a;
    --subhead:#6b5626;
    --note:#b48a4a;
  }
  *{margin:0;padding:0;box-sizing:border-box}
  html,body{width:1200px;height:894px;overflow:hidden;background:var(--backdrop)}
  .canvas{position:relative;width:1200px;height:894px}
  .menu-page{position:absolute;top:115px;width:514px;height:665px;background:var(--paper);color:var(--ink);font-family:"Poppins",sans-serif}
  .menu-page--drinks{left:82px}
  .menu-page--food{left:624px}
  .page-frame{position:absolute;left:15px;top:17px;width:485px;height:632px;border:1.5px solid var(--gold)}
  .masthead{position:absolute;top:10px;left:0;width:100%;height:70px}
  .masthead-name{position:absolute;left:50%;transform:translateX(-50%);top:0;width:150px;height:66px;background:var(--paper);text-align:center;font-family:"Cinzel",serif;color:var(--gold)}
  .menu-page--drinks .masthead-name{left:258px}
  .masthead-name .kicker{display:block;font-size:12px;letter-spacing:2px;line-height:14px;margin-top:5px}
  .masthead-name .name{display:block;font-size:25px;letter-spacing:1px;line-height:26px}
  .masthead-word{position:absolute;top:23px;font-family:"Oswald",sans-serif;font-weight:600;font-size:33px;color:var(--gold);letter-spacing:.5px;background:var(--paper);padding:0 4px}
  .ornament{position:absolute;background:radial-gradient(ellipse at center,var(--gold-soft),rgba(198,168,102,0) 70%)}
  .ribbon{position:absolute;height:20px;background:var(--gold);color:#fff;font-family:"Roboto Condensed",sans-serif;font-weight:500;font-size:13px;line-height:20px;text-align:center;clip-path:polygon(0 0,100% 0,95% 50%,100% 100%,0 100%,5% 50%)}
  .col{position:absolute}
  .item{position:absolute;left:0}
  .item-name{font-family:"Zilla Slab",serif;font-weight:700;font-size:10.5px;line-height:12px;color:var(--ink)}
  .item-name--small{font-size:8px}
  .item-desc{font-size:7px;line-height:9px;color:var(--ink-soft);margin-top:3px}
  .price{position:absolute;top:0;font-family:"Zilla Slab",serif;font-weight:600;font-size:6.5px;color:var(--ink)}
  .price sup{font-size:4px}
  .col--cocktails{left:46px;width:200px}.col--cocktails .price{left:178px}.col--cocktails .item-desc{width:150px}
  .col--wines{left:273px;width:195px}.col--wines .price{left:182px}
  .wine-group{position:absolute;left:0;font-family:"Zilla Slab",serif;font-weight:700;font-size:10px;color:var(--subhead)}
  .wine-label{font-weight:700;font-size:6.8px;line-height:8px}
  .wine-maker{font-size:7px;line-height:9px;color:var(--ink-soft)}
  .boxed-panel{position:absolute;border:1.5px solid var(--gold);border-radius:6px}
  .col--zero{left:282px}.col--zero .price{left:158px}.col--zero .item-desc{width:160px;margin-top:1px}
  .col--food-left{left:46px}.col--food-left .price{left:174px}.col--food-left .item-desc{width:165px}
  .col--food-right{left:280px}.col--food-right .price{left:149px}.col--food-right .item-desc{width:140px}
  .board{position:absolute;left:256px;width:204px;text-align:center}
  .board-item{position:absolute;left:0;width:204px}
  .board-item .item-name{font-size:10.5px}
  .board-price{font-family:"Zilla Slab",serif;font-size:6px;color:var(--gold);display:block;margin-top:3px}
  .board-note{position:absolute;left:0;width:204px;font-family:"Zilla Slab",serif;font-weight:600;font-size:8px;line-height:12px;color:var(--note)}
</style>
</head>
<body>
<main class="canvas">

  <!-- Drinks page -->
  <section class="menu-page menu-page--drinks">
    <div class="page-frame"></div>
    <div class="ornament" style="left:12px;top:12px;width:50px;height:40px" role="img" aria-label="Gold floral corner flourish"></div>
    <div class="ornament" style="right:12px;top:12px;width:50px;height:40px" role="img" aria-label="Gold floral corner flourish"></div>
    <div class="ornament" style="left:12px;bottom:12px;width:50px;height:40px" role="img" aria-label="Gold floral corner flourish"></div>
    <div class="ornament" style="right:12px;bottom:12px;width:50px;height:40px" role="img" aria-label="Gold floral corner flourish"></div>
    <div class="ornament" style="left:160px;bottom:0;width:200px;height:36px" role="img" aria-label="Gold vine and flower border ornament"></div>
    <div class="ornament" style="left:4px;top:160px;width:30px;height:60px" role="img" aria-label="Gold vine swirl"></div>
    <div class="ornament" style="right:0;top:310px;width:30px;height:60px" role="img" aria-label="Gold vine swirl"></div>

    <header class="masthead">
      <span class="masthead-word" style="left:76px">DRINKS</span>
      <div class="masthead-name"><span class="kicker">BISTRO</span><span class="name">MARLOWE</span></div>
      <div class="ornament" style="left:238px;top:56px;width:40px;height:18px" role="img" aria-label="Small gold flower ornament"></div>
      <span class="masthead-word" style="left:330px">MENU</span>
    </header>

    <div class="ribbon" style="left:46px;top:95px;width:162px">French Bistro Cocktails</div>
    <div class="col col--cocktails">
      <div class="item" style="top:122px"><p class="item-name">French 75</p><p class="item-desc">Gin, fresh lemon juice, simple syrup, topped with Champagne.</p><span class="price"><sup>$</sup>18</span></div>
      <div class="item" style="top:161px"><p class="item-name">Sidecar</p><p class="item-desc">Cognac, Triple Sec, and fresh lemon juice with a sugared rim.</p><span class="price"><sup>$</sup>18</span></div>
      <div class="item" style="top:203px"><p class="item-name">Boulevardier</p><p class="item-desc" style="width:170px">Bourbon, Bitter Aperitivo, and Sweet Vermouth.</p><span class="price"><sup>$</sup>18</span></div>
      <div class="item" style="top:237px"><p class="item-name">Kir Royale</p><p class="item-desc">Crème de Cassis topped with chilled Champagne.</p><span class="price"><sup>$</sup>18</span></div>
      <div class="item" style="top:284px"><p class="item-name item-name--small">Lavender Martini</p><p class="item-desc" style="font-size:7.8px;line-height:10px">Vodka, house-made lavender syrup, and dry vermouth.</p><span class="price"><sup>$</sup>18</span></div>
    </div>

    <div class="ribbon" style="left:46px;top:347px;width:154px">Other Beverages</div>
    <div class="col col--cocktails">
      <div class="item" style="top:379px"><p class="item-name">Diabolo Menthe</p><p class="item-desc" style="width:170px">Refreshing peppermint syrup topped with chilled lemonade and a sprig of fresh mint.</p><span class="price"><sup>$</sup>18</span></div>
      <div class="item" style="top:431px"><p class="item-name">Orangeade</p><p class="item-desc" style="width:170px">The classic French citrus sparkling juice with natural orange pulp and zest.</p><span class="price"><sup>$</sup>18</span></div>
      <div class="item" style="top:476px"><p class="item-name">Café au Lait</p><p class="item-desc" style="width:165px">A bold double shot of espresso served in a traditional bowl with an equal part of steamed milk.</p><span class="price"><sup>$</sup>18</span></div>
      <div class="item" style="top:529px"><p class="item-name">Espresso / Americano</p><span class="price"><sup>$</sup>18</span></div>
      <div class="item" style="top:547px"><p class="item-name">Chocolat Chaud Maison</p><p class="item-desc" style="width:175px">Our signature "Parisian style" hot chocolate—thick, melted 70% dark chocolate served with a side of fresh Chantilly cream.</p><span class="price"><sup>$</sup>18</span></div>
    </div>

    <div class="ribbon" style="left:273px;top:96px;width:161px">Wines by the Glass</div>
    <div class="col col--wines">
      <p class="wine-group" style="top:123px">White Wine | Vins Blancs</p>
      <div class="item" style="top:143px"><p class="wine-label">House White:</p><p class="wine-maker">Cuvée Armand (Chardonnay Blend)</p><span class="price"><sup>$</sup>12</span></div>
      <div class="item" style="top:166px"><p class="wine-label">Muscadet Sèvre et Maine:</p><p class="wine-maker">Sur Lie</p><span class="price"><sup>$</sup>12</span></div>
      <div class="item" style="top:190px"><p class="wine-label">Sauvignon Blanc:</p><p class="wine-maker">Domaine des Saulaies</p><span class="price"><sup>$</sup>12</span></div>
      <div class="item" style="top:214px"><p class="wine-label">Chardonnay:</p><p class="wine-maker">Domaine Ferrand</p><span class="price"><sup>$</sup>12</span></div>
      <div class="item" style="top:238px"><p class="wine-label">Riesling:</p><p class="wine-maker">Alsace Tradition</p><span class="price"><sup>$</sup>12</span></div>
      <p class="wine-group" style="top:271px">Red Wines | Vins Rouges</p>
      <div class="item" style="top:286px"><p class="wine-label">House Red:</p><p class="wine-maker">Cuvée Armand (Grenache/Syrah)</p><span class="price"><sup>$</sup>12</span></div>
      <div class="item" style="top:309px"><p class="wine-label">Gamay:</p><p class="wine-maker">Beaujolais-Villages</p><span class="price"><sup>$</sup>12</span></div>
      <div class="item" style="top:334px"><p class="wine-label">Pinot Noir:</p><p class="wine-maker">Bourgogne Rouge</p><span class="price"><sup>$</sup>12</span></div>
      <div class="item" style="top:358px"><p class="wine-label">Cabernet Franc:</p><p class="wine-maker">Chinon "Les Prés"</p><span class="price"><sup>$</sup>12</span></div>
      <div class="item" style="top:382px"><p class="wine-label">Grenache Blend:</p><p class="wine-maker">Côtes du Rhône</p><span class="price"><sup>$</sup>12</span></div>
    </div>

    <div class="boxed-panel" style="left:265px;top:426px;width:205px;height:168px"></div>
    <div class="ribbon" style="left:282px;top:414px;width:160px">Zero Proof Options</div>
    <div class="col col--zero">
      <div class="item" style="top:443px"><p class="item-name">Kir/Kir Royale</p><p class="item-desc">Non-alcoholic wine or sparkling cider with a splash of cassis (blackcurrant) syrup.</p><span class="price"><sup>$</sup>18</span></div>
      <div class="item" style="top:484px"><p class="item-name">Diabolo Menthe/Grenadine</p><p class="item-desc" style="width:140px">Lemonade or soda water with mint (menthe) or grenadine syrup.</p><span class="price"><sup>$</sup>18</span></div>
      <div class="item" style="top:521px"><p class="item-name">Anise-Flavored Spritzer</p><p class="item-desc" style="width:150px">Non-alcoholic spirit with anise/licorice notes mixed with water</p><span class="price"><sup>$</sup>18</span></div>
      <div class="item" style="top:558px"><p class="item-name">Orgeat-Based Drinks</p><p class="item-desc" style="width:150px">Almond syrup (orgeat) mixed with pineapple, lime, or other fruit juices</p><span class="price"><sup>$</sup>18</span></div>
    </div>
  </section>

  <!-- Food page -->
  <section class="menu-page menu-page--food">
    <div class="page-frame"></div>
    <div class="ornament" style="left:12px;top:12px;width:50px;height:40px" role="img" aria-label="Gold floral corner flourish"></div>
    <div class="ornament" style="right:12px;top:12px;width:50px;height:40px" role="img" aria-label="Gold floral corner flourish"></div>
    <div class="ornament" style="left:12px;bottom:12px;width:50px;height:40px" role="img" aria-label="Gold floral corner flourish"></div>
    <div class="ornament" style="right:12px;bottom:12px;width:50px;height:40px" role="img" aria-label="Gold floral corner flourish"></div>
    <div class="ornament" style="left:160px;bottom:0;width:200px;height:36px" role="img" aria-label="Gold vine and flower border ornament"></div>
    <div class="ornament" style="left:0;top:160px;width:30px;height:60px" role="img" aria-label="Gold vine swirl"></div>
    <div class="ornament" style="right:0;top:310px;width:30px;height:60px" role="img" aria-label="Gold vine swirl"></div>

    <header class="masthead">
      <div class="masthead-name"><span class="kicker">BISTRO</span><span class="name">MARLOWE</span></div>
      <div class="ornament" style="left:237px;top:56px;width:40px;height:18px" role="img" aria-label="Small gold flower ornament"></div>
    </header>

    <div class="ribbon" style="left:46px;top:95px;width:150px">Appetizers</div>
    <div class="col col--food-left">
      <div class="item" style="top:122px"><p class="item-name">Escargots de Bourgogne</p><p class="item-desc">Six snails in garlic-parsley butter with toasted baguette.</p><span class="price"><sup>$</sup>18</span></div>
      <div class="item" style="top:162px"><p class="item-name">Truffle Frites</p><p class="item-desc">Hand-cut fries, truffle oil, Parmesan, and garlic aioli.</p><span class="price"><sup>$</sup>18</span></div>
      <div class="item" style="top:205px"><p class="item-name">Baked Brie en Croûte</p><p class="item-desc">A wheel of creamy triple-cream Brie wrapped in flaky, golden puff pastry.</p><span class="price"><sup>$</sup>18</span></div>
      <div class="item" style="top:251px"><p class="item-name">Pâté de Campagne</p><p class="item-desc">A rustic, house-made country pâté of pork and herbs.</p><span class="price"><sup>$</sup>18</span></div>
      <div class="item" style="top:295px"><p class="item-name">Tarte Flambée</p><p class="item-desc">An Alsatian-style "flatbread" with a thin, crispy crust, topped with crème fraîche, caramelized onions</p><span class="price"><sup>$</sup>18</span></div>
    </div>

    <div class="ribbon" style="left:46px;top:358px;width:150px">Entrees</div>
    <div class="col col--food-left">
      <div class="item" style="top:389px"><p class="item-name">Steak Frites</p><p class="item-desc">Pan-seared steak (often sirloin or flank) with a rich sauce</p><span class="price"><sup>$</sup>18</span></div>
      <div class="item" style="top:431px"><p class="item-name">Boeuf Bourguignon</p><p class="item-desc">A rich beef stew braised with red wine, mushrooms, onions, and bacon.</p><span class="price"><sup>$</sup>18</span></div>
      <div class="item" style="top:474px"><p class="item-name">Coq au Vin</p><p class="item-desc" style="width:170px">Chicken braised with red wine, mushrooms, onions, and sometimes lardons.</p><span class="price"><sup>$</sup>18</span></div>
      <div class="item" style="top:514px"><p class="item-name">Duck Confit</p><p class="item-desc">Duck legs cured and slow-cooked in their own fat until tender and crispy.</p><span class="price"><sup>$</sup>18</span></div>
      <div class="item" style="top:557px"><p class="item-name">Moules-Frites</p><p class="item-desc">Mussels steamed in white wine or cream, served with fries.</p><span class="price"><sup>$</sup>18</span></div>
    </div>

    <div class="ribbon" style="left:282px;top:96px;width:152px">Soups &amp; Salads</div>
    <div class="col col--food-right">
      <div class="item" style="top:125px"><p class="item-name">French Onion Soup</p><p class="item-desc">Caramelized onions, beef broth, sourdough crouton, and melted Gruyère.</p><span class="price" style="top:2px"><sup>$</sup>18</span></div>
      <div class="item" style="top:181px"><p class="item-name">Salade Verte</p><p class="item-desc">Mixed baby greens, shaved radishes, and herbs with a Champagne vinaigrette.</p><span class="price"><sup>$</sup>18</span></div>
      <div class="item" style="top:241px"><p class="item-name">Classic Niçoise</p><p class="item-desc">Seared ahi tuna, haricots verts, fingerling potatoes, hard-boiled egg, and olives over butter lettuce.</p><span class="price"><sup>$</sup>18</span></div>
      <div class="item" style="top:306px"><p class="item-name">Velouté de Champignons<br>&nbsp;Sauvages</p><p class="item-desc" style="width:150px">A silky, cream-based soup featuring a blend of roasted cremini</p><span class="price"><sup>$</sup>18</span></div>
    </div>

    <div class="boxed-panel" style="left:256px;top:384px;width:204px;height:215px"></div>
    <div class="ribbon" style="left:280px;top:372px;width:150px">Charcuterie &amp; Fromage</div>
    <div class="board">
      <div class="board-item" style="top:400px"><p class="item-name">Chicken liver pate</p><span class="board-price">$18</span></div>
      <div class="board-item" style="top:430px"><p class="item-name">Country pork and<br>pistachio terrine</p><span class="board-price">$18</span></div>
      <div class="board-item" style="top:473px"><p class="item-name">Fromage de tete</p><span class="board-price">$18</span></div>
      <div class="board-item" style="top:506px"><p class="item-name">Jambon</p><span class="board-price">$18</span></div>
      <div class="board-item" style="top:539px"><p class="item-name">Saucisson sec</p><span class="board-price">$18</span></div>
      <p class="board-note" style="top:568px">Item comes with house made pickles,<br>bread, mustard, etc.</p>
    </div>
  </section>

</main>
</body>
</html>
```